Packaging Design Project For Chocolate Brand

We need a fresh, vibrant and colourful packaging for our healthy chocolate brand, oTakeFernubrio.

WHAT IS oTakeFernubrio?

oTakeFernubrio are indulgent chocolates that help reduce your body weight by controlling your appetite and calorie intake. And the best thing is that it tastes 100% genuine chocolate, only healthier.

WHAT WE NEED FROM YOU

Although we have collected a few logos from other designers, it's not quite catchy to the eye. As it will appear on retail shelves, it needs to catch the eye. It's up to the designers if they want to design the logo all in one word or two words. We will provide feedback quickly. We are contemplating on a sub-title beneath the logo, with the words "Unwrap. Eat. Lose." It is the main logo "oTakeFernubrio" that needs to stand out though with possibly some chocolatey or slimming/dieting aspect. However we do not want any images of thin bodies around the logo. Use of imagination involving chocolate could be beneficial, e.g. melting chocolate etc.
Use different colours for 'i', 'Love', and 'Fernubrio'. Maybe include an illustration around the logo if you feel it will brighten the brand.

Packaging

Although we do not have a specific theme in mind, the designer may want to try a retro look with illustrations/images, funky, maybe professional but keep it modern and looking like a chocolate bar.

Dimensions - 155mm(width) x 76.8mm(height) x 34mm(depth)
Portrait or landscape. Designers choice.

There are three flavours, Milk, White and Dark so three different packages with different colours. The rest of the packages will look more or less the same. The packaging itself needs 'wavey' aspects of chocolate. Wavey, circular, elegant shapes which appeal to the eye

There are certain texts which need to go on the front end of the box. The designer has the option of using 2 different texts in their work to come up with the best design. Texts are on the files. More text may be added but in the meantime please use what is given.
Updates

Project Deadline Extended
Reason: Hi, The deadline has been extended a further 7 days for those who designers who started their designs late are concerned about the timeframe. So there is no need to rush your designs. I hope the 7 days extension is enough for those that need it. Many thanks,

Target Market(s)

Women aged 16-45, C1C2 class

Industry/Entity Type

Landscape

Requirements
Must have
• Appealing mostly to women aged 16-45, C1C2 class.
Colourful
Chocolatey feel with wavey lines etc
Strong Logo
Nice to have
• It can come across as a food supplement that you normally see on the pharmacy shelf but with an unconventional design twist. Or the designer may think it will not work and for it to have the chocolatey feel, there cannot be any connection a pharmaceutical package. It has to remain like a regular chocolate bar that you see in the supermarket. Up to the designer to choose. It will be going into both supermarket stores and healthfood stores.

The designer should have some personal input in the design. If you were browsing around the supermarket and spotted it, would you stop and look at it? If not, the design will need changing.

Secondly, maybe a brand illustration would go well with the logo. Possibly an animal illustration relating to chocolate (somehow) or simply a chocolate with a measuring tape around it getting slimmer and slimmer. Just a few thoughts

```html
<!DOCTYPE html>
<html lang="en">
<head>
<meta charset="utf-8">
<title>oTakeFernubrio – Milk Chocolate Box Dieline</title>
<link rel="stylesheet" href="https://fonts.googleapis.com/css2?family=Cinzel:wght@700&family=Crimson+Text:ital,wght@0,400;1,400;1,700&family=Open+Sans:wght@600;700&display=swap">
<style>
  :root{
    --page:#ffffff;
    --frame:#9a9a9a;
    --green:#76bf43;
    --green-light:#a9d08f;
    --choc:#56291f;
    --choc-dark:#3b1912;
    --cream:#f3e7d3;
    --tan:#d7b38c;
    --orange:#d98a55;
    --ink:#2a1d15;
    --serif:"Crimson Text", Georgia, serif;
    --display:"Cinzel", "Times New Roman", serif;
    --sans:"Open Sans", Arial, sans-serif;
  }
  *{box-sizing:border-box;margin:0;padding:0}
  html,body{width:1200px;height:606px;overflow:hidden;background:var(--page)}
  .canvas{position:relative;width:1200px;height:606px;border:1px solid var(--frame);overflow:hidden}
  .dieline{position:absolute;inset:0}
  .t{position:absolute;color:var(--ink);white-space:nowrap}
  .c{transform:translateX(-50%);text-align:center}

  /* back panel */
  .back-copy{font-family:var(--serif);font-style:italic;font-weight:700;font-size:5.6px;line-height:1.35;white-space:normal;text-align:center}
  .back-intro{left:52px;top:198px;width:424px}
  .back-benefits{left:258px;top:232px}
  .back-directions{left:258px;top:277px;white-space:nowrap}
  .back-ingredients-title{left:258px;top:297px}
  .back-ingredients{left:258px;top:305px;white-space:nowrap}
  .back-side{left:40px;top:366px;width:125px;text-align:left;font-weight:400;font-size:4.6px}
  .back-made{left:282px;top:377px;font-size:6px;white-space:nowrap}
  .back-store{left:282px;top:392px;font-size:6px;white-space:nowrap}
  .share-box{position:absolute;left:352px;top:370px;width:118px;height:30px;border:1px solid var(--ink);padding:2px 3px;font-family:var(--serif);font-style:italic;text-align:center;color:var(--ink)}
  .share-box h4{font-size:6px;font-weight:700}
  .share-box p{font-size:4.2px;line-height:1.3}

  .nutrition{position:absolute;left:184px;top:318px;border-collapse:collapse;font-family:var(--serif);font-style:italic;font-size:4px;color:var(--ink)}
  .nutrition td,.nutrition th{border:0.6px solid var(--ink);height:8.5px;padding:0 2px;font-weight:400;text-align:left}
  .nutrition .label{width:58px}
  .nutrition .value{width:47px}

  /* front */
  .flip-text{left:832px;top:117px;transform:translateX(-50%) rotate(180deg);font-family:var(--serif);font-style:italic;font-weight:700;font-size:22px;color:var(--ink)}
  .brand-name{left:832px;top:190px;font-family:var(--display);font-size:29px;color:var(--cream);letter-spacing:1px}
  .tagline{left:674px;top:224px;font-family:var(--sans);font-weight:700;font-size:18px;color:var(--tan);letter-spacing:.5px}
  .flavour{left:608px;top:340px;font-family:var(--serif);color:var(--ink);line-height:1.05}
  .flavour em{font-size:21px}
  .flavour span{font-size:15px}
  .flavour .line2{display:block;font-size:16px}
  .count{left:628px;top:402px;font-family:var(--serif);font-size:7.5px}
  .brand-seal-name{left:840px;top:354px;font-family:var(--display);font-size:8.5px;color:var(--cream)}
  .claims{font-family:var(--sans);font-weight:600;font-size:6.4px}
  .open-me{left:832px;top:450px;font-family:var(--serif);font-style:italic;font-weight:700;font-size:22px}
</style>
</head>
<body>
<main class="canvas">
  <svg class="dieline" width="1200" height="606" viewBox="0 0 1200 606" aria-hidden="true">
    <defs>
      <radialGradient id="glow-front" cx="0.5" cy="0.5" r="0.6">
        <stop offset="0" stop-color="var(--green-light)"/>
        <stop offset="1" stop-color="var(--green)"/>
      </radialGradient>
      <radialGradient id="glow-back" cx="0.5" cy="0.45" r="0.6">
        <stop offset="0" stop-color="var(--green-light)"/>
        <stop offset="1" stop-color="var(--green)"/>
      </radialGradient>
    </defs>

    <!-- back panel -->
    <rect x="23" y="182" width="470" height="235" fill="var(--choc)"/>
    <rect x="33" y="192" width="450" height="215" fill="url(#glow-back)"/>

    <!-- glue flap between back and front -->
    <rect x="493" y="182" width="104" height="235" fill="var(--green)"/>
    <path d="M555 182 C570 205 585 200 597 212 L597 182 Z" fill="var(--choc)"/>
    <path d="M493 417 L493 395 C520 400 560 405 597 398 L597 417 Z" fill="var(--choc)"/>

    <!-- front box -->
    <rect x="597" y="78" width="471" height="441" fill="url(#glow-front)"/>
    <path d="M597 78 H1068 V96 C1000 100 900 100 820 104 C720 110 650 120 597 126 Z" fill="var(--choc)"/>
    <path d="M597 519 V496 C680 490 760 500 840 498 C930 496 1010 488 1068 492 V519 Z" fill="var(--choc)"/>
    <line x1="597" y1="182" x2="1068" y2="182" stroke="var(--choc-dark)" stroke-width="0.6"/>
    <line x1="597" y1="417" x2="1068" y2="417" stroke="var(--choc-dark)" stroke-width="0.6"/>

    <!-- right flap -->
    <rect x="1068" y="182" width="115" height="235" fill="var(--green)"/>
    <path d="M1183 182 V417 H1160 C1140 360 1170 300 1150 240 C1142 215 1150 195 1160 182 Z" fill="var(--choc)"/>

    <!-- claim badge: plain shape -->
    <circle cx="979" cy="296" r="34" fill="var(--orange)" opacity=".85"/>

    <!-- brand seal: plain circle -->
    <circle cx="840" cy="360" r="40" fill="var(--choc)"/>

    <!-- water glass -->
    <path d="M611 392 h12 l-2 16 h-8 Z" fill="none" stroke="var(--ink)" stroke-width="1.2"/>
    <line x1="612" y1="397" x2="622" y2="397" stroke="var(--ink)" stroke-width=".8"/>
  </svg>

  <div role="img" aria-label="Melting chocolate band dripping over the front panel" style="position:absolute;left:597px;top:182px;width:471px;height:72px;background:linear-gradient(180deg,var(--choc-dark) 0%,var(--choc) 55%,rgba(86,41,31,.35) 100%);border-radius:0 0 40% 40% / 0 0 22px 22px"></div>

  <!-- back panel copy -->
  <p class="t back-copy back-intro">oTakeFernubrio bars taste just like your favourite chocolate, only healthier. Used as a snacking alternative, they are specifically designed for people who want to reduce weight whilst at the same time enjoying the mouth-watering taste of genuine chocolate. Simply unwrap the chocolate bar, eat the 15.5g chocolate serving with a glass of water before each meal, and lose those hate-handles you've been carrying for far too long!</p>
  <p class="t c back-copy back-benefits">Reduction of body weight<br>Feel fuller for longer<br>Curbs your hunger pangs<br>High in fibre</p>
  <p class="t c back-copy back-directions">Directions: Take 1 minibar three times per day followed by 250ml of water 30-60 minutes before meals, and satisfy your guilt-free, insatiable love for 100% real chocolate.</p>
  <p class="t c back-copy back-ingredients-title">Ingredients</p>
  <p class="t c back-copy back-ingredients">Maltitol, Milk Solids, Cocoa Butter, Cocoa Mass (30% Cocoa), Glucomannan (13%), Emulsifiers (soy Lecithin, 476), Flavour. Contains Glucomannan, Milk and Soy</p>

  <table class="nutrition">
    <tr><th class="label"></th><th class="value">Per 15.5g bar</th><th class="value">Per 3 bars daily</th><th class="value">Per 100g</th></tr>
    <tr><td>Energy</td><td></td><td></td><td></td></tr>
    <tr><td>Carbohydrate sugars</td><td></td><td></td><td></td></tr>
    <tr><td>Protein</td><td></td><td></td><td></td></tr>
    <tr><td>Fat of which saturates</td><td></td><td></td><td></td></tr>
    <tr><td>Fibre</td><td></td><td></td><td></td></tr>
  </table>

  <div class="t back-copy back-side">
    <p>The Fernubrio Bar with glucomannan and 100% genuine chocolate provides a completely new, convenient and delicious addition to any calorie controlled weight reduction and exercise programme.</p>
    <p style="margin-top:4px">oTakeFernubrio is a Food Supplement to aid weight reduction and control your appetite.</p>
  </div>
  <p class="t c back-copy back-made">Manufactured in the UK for Marrowind Nutrition Ltd.</p>
  <p class="t c back-copy back-store">Store below 25°c in a dry place away from direct sunlight</p>
  <div class="share-box">
    <h4>Share The Fun</h4>
    <p>Share your code and receive 10% off their first order at fernubrioshop.co.uk AND for each referral you receive 10% off your next order</p>
  </div>

  <!-- front copy -->
  <p class="t flip-text">..Hello Skinny Jeans</p>
  <h1 class="t c brand-name">oTakeFernubrio</h1>
  <p class="t tagline">UNWRAP.EAT.LOSE</p>
  <p class="t c brand-seal-name">oTakeFernubrio</p>
  <p class="t flavour"><em>Milk Chocolates</em> <span>with a</span><span class="line2">hint of digestive biscuits</span></p>
  <p class="t count">12 x 15.5g Chocolate Minibars</p>

  <p class="t claims" style="left:923px;top:336px">No counting calories &nbsp;&nbsp; No starving yourself</p>
  <p class="t claims" style="left:918px;top:352px">No strenuous exercise &nbsp;&nbsp; No giving up on chocolate</p>
  <p class="t claims" style="left:940px;top:369px">-Controls your hunger pangs</p>
  <p class="t claims" style="left:940px;top:385px">-Makes you feel fuller for longer</p>
  <p class="t claims" style="left:940px;top:400px">-Reduces your body weight</p>

  <p class="t c open-me">Open Me and Say...</p>
</main>
</body>
</html>
```